New Board Game - TRY 45:35:20

The project is in two phases:
A. GAME BOARD DESIGN
Design of a striking game board.
NB. See the following files:
* TRY 45:35:20 Background Info
* TRY 45:35:20 Game Board Format
NB. The contest fee is for Phase A only. Additional fees will be paid for Phase B.
B. APPLICATION OF GAME BOARD DESIGN
The game board design will to be applied to the following game materials:
* Game cards (front and back)
* Sticker for game board tube
* Facilitator's Handbook front and back cover
* Icon for pages inside Facilitator's Handbook
Additional information on the game cards will be provided to the winning designer.
Please note that the project fee is for Phase A only. We will pay additional fees for Phase B, i.e. game cards etc.
NOTE:
Please keep in mind that the game will be used in a corporate setting. The initial target group are Learning and Development (L&D) specialists, mainly people who develop or deliver training courses. They are all educated professionals.
I recently included this feedback in a message to one of the designers:
The game board has to have a level of sophistication and elegance that suits a corporate environment. The game will also be the first direct contact that some potential members will have with the Collegium and has to make a positive impression on them.
We want people to perceive the game as a top-class, creative product.
PLEASE NOTE:
The project fee is now a guaranteed payment.
Target Market(s)
The game will initially be used at networking events held by the Collegium of Skill Advisors in Australia (see: www.csaglobalnet.org). These events are attended by members and guests, with the group ranging from 10 to 20 attendees.
The game may also be used as part of management or leadership development programs in business and government organisations.
Another possible use is with teachers at networking events or professional development courses.
Requirements
Must have
- See the uploaded files for important design requirements.
What is most important is that the game materials are attractive, appealing, impactful. People (in the target group) who see the game materials should feel that they want to find out more, pick up the cards and play the game.
Should not have
- Still thinking....

```html
<!DOCTYPE html>
<html lang="en">
<head>
<meta charset="utf-8">
<title>TRY 45:35:20 – Game Board</title>
<link rel="stylesheet" href="https://fonts.googleapis.com/css2?family=Oswald:wght@300;600&display=swap">
<style>
  :root {
    --red: #ed1c24;
    --green: #8dc63f;
    --yellow: #fff200;
    --orange: #f15a29;
    --blue: #27aae1;
    --purple: #662d91;
    --paper: #f1f1f2;
    --ink: #1a1a1a;
    --white: #ffffff;
    --sack: #e6dcb4;
    --coin: #e2b32c;
  }
  html, body {
    margin: 0;
    padding: 0;
    width: 1200px;
    height: 996px;
    overflow: hidden;
    background: var(--paper);
  }
  .board { display: block; width: 1200px; height: 996px; }
  .tile-label {
    font-family: "Oswald", sans-serif;
    font-weight: 300;
    font-size: 31px;
    fill: var(--ink);
    text-anchor: middle;
    dominant-baseline: central;
  }
  .game-title {
    font-family: "Oswald", sans-serif;
    font-weight: 600;
    fill: var(--white);
    text-anchor: middle;
  }
  .red { fill: var(--red); }
  .green { fill: var(--green); }
  .yellow { fill: var(--yellow); }
  .orange { fill: var(--orange); }
  .blue { fill: var(--blue); }
  .centre-field { fill: var(--purple); }
  .card { fill: var(--white); stroke: var(--green); stroke-width: 6; }
  .card--featured { stroke: var(--yellow); }
</style>
</head>
<body>
<svg class="board" viewBox="0 0 1247 1035" xmlns="http://www.w3.org/2000/svg">
  <rect class="centre-field" x="151" y="168" width="945" height="705"/>

  <!-- top row -->
  <g class="track track--top">
    <rect class="red" x="15" y="25" width="123" height="127"/>
    <text class="tile-label" transform="translate(76 88) rotate(90)">YIKES!!</text>
    <rect class="green" x="151" y="25" width="124" height="127"/>
    <text class="tile-label" x="213" y="92">20%</text>
    <rect class="yellow" x="288" y="25" width="124" height="127"/>
    <text class="tile-label" x="344" y="70">ROLL</text>
    <text class="tile-label" x="344" y="112">AGAIN</text>
    <rect class="orange" x="425" y="25" width="124" height="127"/>
    <text class="tile-label" x="487" y="92">70%</text>
    <rect class="orange" x="562" y="25" width="124" height="127"/>
    <text class="tile-label" x="624" y="92">70%</text>
    <rect class="orange" x="698" y="25" width="124" height="127"/>
    <text class="tile-label" x="760" y="92">70%</text>
    <rect class="yellow" x="835" y="25" width="124" height="127"/>
    <text class="tile-label" x="897" y="70">ANY</text>
    <text class="tile-label" x="897" y="112">CARD</text>
    <rect class="blue" x="972" y="25" width="123" height="127"/>
    <text class="tile-label" x="1028" y="92">10%</text>
    <rect class="red" x="1108" y="25" width="124" height="127"/>
    <text class="tile-label" transform="translate(1170 88) rotate(-90)">OOPS!</text>
  </g>

  <!-- left column -->
  <g class="track track--left">
    <rect class="green" x="15" y="168" width="123" height="128"/>
    <text class="tile-label" transform="translate(74 232) rotate(90)">20%</text>
    <rect class="blue" x="15" y="313" width="123" height="128"/>
    <text class="tile-label" transform="translate(74 377) rotate(90)">10%</text>
    <rect class="yellow" x="15" y="457" width="123" height="128"/>
    <text class="tile-label" transform="translate(92 521) rotate(90)">MISS A</text>
    <text class="tile-label" transform="translate(58 521) rotate(90)">TURN</text>
    <rect class="orange" x="15" y="601" width="123" height="128"/>
    <text class="tile-label" transform="translate(74 665) rotate(90)">70%</text>
    <rect class="orange" x="15" y="745" width="123" height="128"/>
    <text class="tile-label" transform="translate(74 809) rotate(90)">70%</text>
  </g>

  <!-- right column -->
  <g class="track track--right">
    <rect class="green" x="1108" y="168" width="124" height="128"/>
    <text class="tile-label" transform="translate(1170 238) rotate(-90)">20%</text>
    <rect class="green" x="1108" y="313" width="124" height="128"/>
    <text class="tile-label" transform="translate(1170 380) rotate(-90)">20%</text>
    <rect class="yellow" x="1108" y="457" width="124" height="128"/>
    <text class="tile-label" transform="translate(1154 524) rotate(-90)">MISS A</text>
    <text class="tile-label" transform="translate(1188 524) rotate(-90)">TURN</text>
    <rect class="orange" x="1108" y="601" width="124" height="128"/>
    <text class="tile-label" transform="translate(1170 668) rotate(-90)">70%</text>
    <rect class="orange" x="1108" y="745" width="124" height="128"/>
    <text class="tile-label" transform="translate(1170 810) rotate(-90)">70%</text>
  </g>

  <!-- bottom row -->
  <g class="track track--bottom">
    <rect class="red" x="15" y="888" width="123" height="127"/>
    <text class="tile-label" x="77" y="955">UH-OH!</text>
    <rect class="orange" x="151" y="888" width="124" height="127"/>
    <text class="tile-label" x="213" y="955">70%</text>
    <rect class="yellow" x="288" y="888" width="124" height="127"/>
    <text class="tile-label" x="350" y="933">ANY</text>
    <text class="tile-label" x="350" y="975">CARD</text>
    <rect class="green" x="425" y="888" width="124" height="127"/>
    <text class="tile-label" x="493" y="955">20%</text>
    <rect class="green" x="562" y="888" width="124" height="127"/>
    <text class="tile-label" x="624" y="955">20%</text>
    <rect class="blue" x="698" y="888" width="124" height="127"/>
    <text class="tile-label" x="760" y="955">10%</text>
    <rect class="yellow" x="835" y="888" width="124" height="127"/>
    <text class="tile-label" x="897" y="933">ROLL</text>
    <text class="tile-label" x="897" y="975">AGAIN</text>
    <rect class="orange" x="972" y="888" width="123" height="127"/>
    <text class="tile-label" x="1033" y="955">70%</text>
    <rect class="red" x="1108" y="888" width="124" height="127"/>
    <text class="tile-label" x="1170" y="955">CRIKEY!</text>
  </g>

  <!-- centre title -->
  <g class="game-name">
    <text class="game-title" x="655" y="380" font-size="96">TRY</text>
    <text class="game-title" x="655" y="512" font-size="124">45:35:20</text>
  </g>

  <!-- card deck -->
  <g class="card-deck">
    <rect class="card" x="440" y="590" width="125" height="235" rx="10" transform="rotate(-24 502 707)"/>
    <rect class="card" x="745" y="590" width="125" height="235" rx="10" transform="rotate(24 807 707)"/>
    <rect class="card card--featured" x="540" y="565" width="118" height="238" rx="8"/>
    <rect class="card card--featured" x="628" y="563" width="120" height="240" rx="8"/>
  </g>

  <!-- decorative illustrations -->
  <ellipse role="img" aria-label="Illustration of a green sun visor with the game badge" cx="310" cy="350" rx="98" ry="70" fill="var(--green)" transform="rotate(-20 310 350)"/>
  <rect role="img" aria-label="Illustration of a pair of green dice" x="235" y="705" width="140" height="92" rx="12" fill="var(--green)"/>
  <g role="img" aria-label="Illustration of a sack of gold coins with sparkles">
    <ellipse cx="965" cy="655" rx="88" ry="118" fill="var(--sack)"/>
    <ellipse cx="935" cy="760" rx="55" ry="20" fill="var(--coin)"/>
  </g>
</svg>
</body>
</html>
```